Cloud Phone Service Brochure

We need a brochure for a Cloud Phone Service offering that we offer in Canada. We're a small company that cares about our client's success and protects their privacy. We would like to see designs that reflect us as a stable, trustworthy company which is also fast moving and leading edge. We see ourselves more like Zelmo than Hask. Sketch Harbor has built our logo and business card, and we look forward to moving ahead here. I've attached our Business Card file so you have our logo as well as my own shot at some thoughts about content written as a trifold. That specific content does not need to be used, nor does it need to be a trifold. Those phone pictures are the actual phones we use.

```html
<!DOCTYPE html>
<html lang="en">
<head>
<meta charset="utf-8">
<title>Brightwire Cloud Phone Service Brochure</title>
<link href="https://fonts.googleapis.com/css2?family=Roboto:wght@400;500&family=Roboto+Condensed:wght@400;500;700&display=swap" rel="stylesheet">
<style>
:root{
  --bg:#cfd2d5;
  --paper:#ffffff;
  --paper-shade:#eef0f2;
  --blue:#1b8fd8;
  --blue-light:#36b0f0;
  --blue-deep:#0b4d8c;
  --slate:#3f4b57;
  --text:#6e7882;
  --photo-dark:#1e2d3f;
}
*{margin:0;padding:0;box-sizing:border-box}
html,body{width:876px;height:1200px;overflow:hidden}
body{background:var(--bg);position:relative;font-family:"Roboto",Arial,sans-serif;color:var(--text)}
.sheet{position:absolute;left:54px;width:764px;height:538px;background:var(--paper);box-shadow:0 4px 10px rgba(0,0,0,.25);overflow:hidden}
.sheet--outside{top:32px}
.sheet--inside{top:610px}
.panel{position:absolute;top:0;height:100%}
.panel--left{left:0;width:254px;background:linear-gradient(90deg,#fff 70%,var(--paper-shade))}
.panel--mid{left:254px;width:254px}
.panel--right{left:508px;width:256px;background:linear-gradient(90deg,#e9ecef,#fff 30%)}
.panel--blue{background:linear-gradient(160deg,var(--blue-light) 0%,var(--blue) 40%,var(--blue-deep) 100%)}
.abs{position:absolute}
.title{font-family:"Roboto Condensed",Arial,sans-serif;font-weight:700;color:var(--blue);font-size:16px}
.bar{position:absolute;height:19px;background:var(--slate);color:#fff;font-family:"Roboto Condensed",Arial,sans-serif;font-size:13px;line-height:19px;padding-left:16px;white-space:nowrap;clip-path:polygon(0 0,100% 0,calc(100% - 8px) 100%,0 100%)}
.bullets{list-style:none;font-size:11px;line-height:14.5px}
.bullets li::before{content:"• "}
.badges{display:flex;flex-wrap:wrap;gap:6px 8px;width:226px}
.badge{width:42px;height:12px;border-radius:2px;background:#c5ccd3}
.badge--round{width:14px;height:14px;border-radius:50%}
.photo{position:absolute}
.brand{text-align:center;color:#fff;font-family:"Roboto Condensed",Arial,sans-serif}
.brand__name{font-size:19px;font-weight:500;letter-spacing:1px}
.brand__sub{font-size:7px;letter-spacing:4px;display:flex;align-items:center;justify-content:center;gap:6px}
.brand__sub::before,.brand__sub::after{content:"";width:36px;height:1px;background:currentColor}
.contact{color:#fff;font-size:11px;line-height:26px;text-align:center}
.ticks{list-style:none;font-size:11.5px;white-space:nowrap}
.ticks li{display:flex;align-items:center;gap:5px}
.ticks svg{flex:none}
.services{display:grid;grid-template-columns:repeat(3,84px);row-gap:11px;justify-content:center}
.service{text-align:center;color:#fff;font-size:10px;line-height:11px;height:87px;white-space:nowrap}
.service__ring{width:50px;height:50px;margin:0 auto 6px;border:2px solid #fff;border-radius:50%;box-shadow:0 0 0 2px rgba(255,255,255,.25);display:flex;align-items:center;justify-content:center}
.service__ring svg{stroke:#fff;fill:none;stroke-width:2;stroke-linecap:round;stroke-linejoin:round}
</style>
</head>
<body>

<svg width="0" height="0" style="position:absolute">
  <symbol id="tick" viewBox="0 0 10 10"><circle cx="5" cy="5" r="4" fill="none" stroke="#1b8fd8" stroke-width="1.3"/><path d="M3 5l1.5 1.5L7 3.8" fill="none" stroke="#1b8fd8" stroke-width="1.3"/></symbol>
</svg>

<section class="sheet sheet--outside">
  <div class="panel panel--left">
    <h2 class="abs title" style="left:16px;top:20px">ABOUT BRIGHTWIRE</h2>
    <div class="bar" style="left:0;top:48px;width:240px">WHO WE ARE</div>
    <ul class="abs bullets" style="left:16px;top:70px">
      <li>70% Renewable Energy</li><li>100% Renewable for 2020</li>
    </ul>
    <div class="bar" style="left:0;top:113px;width:240px">WE GIVE OUR TIME AND SKILLS TO HELP</div>
    <ul class="abs bullets" style="left:16px;top:134px">
      <li>Schools</li><li>Community Associations</li><li>Non-profits</li><li>Renewable Energy Initiatives</li>
    </ul>
    <div class="bar" style="left:0;top:206px;width:240px">OUR PARTNERS</div>
    <div class="abs badges" style="left:18px;top:234px">
      <span class="badge"></span><span class="badge"></span><span class="badge"></span><span class="badge"></span><span class="badge"></span>
      <span class="badge" style="width:30px"></span><span class="badge badge--round"></span><span class="badge" style="width:30px"></span><span class="badge" style="width:36px"></span><span class="badge" style="width:30px"></span><span class="badge badge--round"></span>
    </div>
    <svg class="abs" style="left:0;top:300px" width="254" height="238" viewBox="0 0 254 238">
      <path d="M0 30 Q150 -10 254 180" stroke="var(--slate)" stroke-width="4" fill="none"/>
    </svg>
    <div class="photo" role="img" aria-label="Desk phone, monitor with video call grid, tablet and smartphone" style="left:14px;top:360px;width:230px;height:150px;border-radius:6px;background:linear-gradient(160deg,#4a5561,#22282f 60%,#7d8790)"></div>
  </div>

  <div class="panel panel--mid panel--blue">
    <svg class="abs" style="left:0;top:0" width="254" height="538" viewBox="0 0 254 538">
      <path d="M225 0 Q150 160 254 330" stroke="var(--slate)" stroke-width="5" fill="none"/>
    </svg>
    <div class="photo" role="img" aria-label="Touchscreen desk phone" style="left:58px;top:123px;width:140px;height:140px;border-radius:50%;border:5px solid #fff;box-shadow:0 0 0 4px rgba(255,255,255,.35);background:radial-gradient(circle,#3a424b,#12161b 65%,#dfe3e7 66%)"></div>
    <div class="brand abs" style="left:0;top:310px;width:254px">
      <div class="brand__name">BRIGHTWIRE</div>
      <div class="brand__sub">CONSULTING</div>
    </div>
    <div class="bar" style="left:48px;top:364px;width:176px;padding-left:0;text-align:center;font-size:11px;clip-path:polygon(6px 0,100% 0,calc(100% - 6px) 100%,0 100%)">CONTACT US</div>
    <div class="contact abs" style="left:0;top:441px;width:254px">
      hello@brightwire-example.com<br>555-014-2290 | 1-800-555-0199<br>www.brightwire-example.com
    </div>
  </div>

  <div class="panel panel--right">
    <div class="photo" role="img" aria-label="Businesswoman touching a glowing network of cloud and contact nodes above a city skyline at night" style="left:-16px;top:0;width:272px;height:358px;border-bottom-left-radius:75% 35%;background:radial-gradient(circle at 50% 60%,#9aa7b6 0%,#3b4d63 30%,var(--photo-dark) 75%)"></div>
    <h2 class="abs" style="left:10px;top:22px;width:240px;text-align:center;color:#fff;font-family:'Roboto Condensed',Arial,sans-serif;font-weight:500;font-size:16px;line-height:19px">A CLOUD-BASED PHONE SYSTEM<br>FOR BUSINESSES</h2>
    <div class="brand abs" style="left:0;top:460px;width:256px;color:var(--blue)">
      <div class="brand__name" style="color:var(--slate);font-size:20px">BRIGHTWIRE</div>
      <div class="brand__sub">CONSULTING</div>
    </div>
    <div class="bar" style="left:34px;top:508px;width:222px;height:24px;line-height:24px;font-size:14px;clip-path:polygon(8px 0,100% 0,100% 100%,0 100%)">◉ www.brightwire-example.com</div>
  </div>
</section>

<section class="sheet sheet--inside">
  <div class="panel panel--left">
    <div class="photo" role="img" aria-label="Smiling woman talking on a desk phone in an office" style="left:0;top:0;width:254px;height:254px;background:linear-gradient(150deg,#d7dde3,#9fb2c2 45%,#5a7f9e)"></div>
    <div class="photo" role="img" aria-label="Desk phone with colour display" style="left:130px;top:140px;width:110px;height:110px;border-radius:50%;border:5px solid #fff;box-shadow:0 0 0 3px #c8ced4;background:radial-gradient(circle,#3a424b,#12161b 60%,#eef0f2 61%)"></div>
    <div class="bar" style="left:0;top:260px;width:240px">Cloud Phone Service</div>
    <ul class="abs ticks" style="left:18px;top:290px;line-height:19.9px">
      <li><svg width="9" height="9"><use href="#tick"/></svg>No hardware or installation costs</li>
      <li><svg width="9" height="9"><use href="#tick"/></svg>Conference line included</li>
      <li><svg width="9" height="9"><use href="#tick"/></svg>Toll Free Number</li>
      <li><svg width="9" height="9"><use href="#tick"/></svg>North American Long Distance</li>
      <li><svg width="9" height="9"><use href="#tick"/></svg>Monthly billing</li>
      <li><svg width="9" height="9"><use href="#tick"/></svg>Keep your existing phone number</li>
      <li><svg width="9" height="9"><use href="#tick"/></svg>Voicemail to email</li>
      <li><svg width="9" height="9"><use href="#tick"/></svg>Find Me &amp; Follow Me</li>
      <li><svg width="9" height="9"><use href="#tick"/></svg>Call Recording</li>
      <li><svg width="9" height="9"><use href="#tick"/></svg>Desktop and Mobile softphones</li>
      <li><svg width="9" height="9"><use href="#tick"/></svg>Auto Attendant</li>
    </ul>
  </div>

  <div class="panel panel--mid panel--blue">
    <h2 class="abs" style="left:0;top:18px;width:254px;text-align:center;color:#fff;font-family:'Roboto Condensed',Arial,sans-serif;font-weight:700;font-size:17px">OUR SERVICES</h2>
    <div class="abs services" style="left:0;top:50px;width:254px">
      <div class="service"><div class="service__ring"><svg width="26" height="26" viewBox="0 0 26 26"><rect x="10" y="3" width="6" height="5"/><rect x="2" y="18" width="6" height="5"/><rect x="10" y="18" width="6" height="5"/><rect x="18" y="18" width="6" height="5"/><path d="M13 8v10M5 18v-5h16v5"/></svg></div>Network<br>Support</div>
      <div class="service"><div class="service__ring"><svg width="26" height="26" viewBox="0 0 26 26"><rect x="5" y="5" width="16" height="18" rx="2"/><rect x="9" y="8" width="8" height="4"/><path d="M9 16h2M13 16h2M9 19h2M13 19h2"/></svg></div>Phone<br>Service</div>
      <div class="service"><div class="service__ring"><svg width="26" height="26" viewBox="0 0 26 26"><path d="M7 19a5 5 0 0 1 1-10 6 6 0 0 1 11 2 4 4 0 0 1 0 8z"/><rect x="9" y="14" width="8" height="3"/></svg></div>Disaster<br>Recovery</div>

      <div class="service"><div class="service__ring"><svg width="26" height="26" viewBox="0 0 26 26"><rect x="4" y="4" width="15" height="5"/><rect x="4" y="10" width="15" height="5"/><circle cx="18" cy="19" r="4"/></svg></div>Remote<br>Backups</div>
      <div class="service"><div class="service__ring"><svg width="26" height="26" viewBox="0 0 26 26"><path d="M3 10a14 14 0 0 1 20 0M6 14a9 9 0 0 1 14 0M9 17a5 5 0 0 1 8 0"/><circle cx="13" cy="20" r="1"/></svg></div>Wireless coverage<br>planning</div>
      <div class="service"><div class="service__ring"><svg width="26" height="26" viewBox="0 0 26 26"><rect x="3" y="5" width="20" height="13"/><path d="M9 22h8M13 18v4"/></svg></div>Nimbus Office<br>&amp; Docs Apps</div>

      <div class="service"><div class="service__ring"><svg width="26" height="26" viewBox="0 0 26 26"><path d="M13 3 24 22H2z"/><path d="M13 10v5M13 18v1"/></svg></div>Spam &amp;<br>Virus Filtering</div>
      <div class="service"><div class="service__ring"><svg width="26" height="26" viewBox="0 0 26 26"><ellipse cx="13" cy="6" rx="8" ry="3"/><path d="M5 6v14c0 2 16 2 16 0V6M5 11c0 2 16 2 16 0M5 16c0 2 16 2 16 0"/></svg></div>Migration<br>Services</div>
      <div class="service"><div class="service__ring"><svg width="26" height="26" viewBox="0 0 26 26"><rect x="3" y="4" width="20" height="14"/><path d="M9 22h8M13 18v4"/></svg></div>Server &amp; Network<br>Monitoring</div>

      <div class="service"><div class="service__ring"><svg width="26" height="26" viewBox="0 0 26 26"><rect x="8" y="3" width="10" height="6"/><rect x="3" y="9" width="20" height="9" rx="2"/><rect x="8" y="15" width="10" height="7"/></svg></div>Printing, Scanning<br>&amp; Plotting</div>
      <div class="service"><div class="service__ring"><svg width="26" height="26" viewBox="0 0 26 26"><path d="M13 3 22 6v7c0 5-4 8-9 10-5-2-9-5-9-10V6z"/><rect x="10" y="12" width="6" height="5"/><path d="M11 12v-2a2 2 0 0 1 4 0v2"/></svg></div>Firewalls<br>&amp; Security</div>
      <div class="service"><div class="service__ring"><svg width="26" height="26" viewBox="0 0 26 26"><path d="M9 3h9l4 4v14H9z"/><path d="M5 7v17h13"/></svg></div>Network Design<br>&amp; Planning</div>

      <div class="service"><div class="service__ring"><svg width="26" height="26" viewBox="0 0 26 26"><path d="M4 22l5-5M17 9l5-5M9 12l5 5-3 3-5-5zM12 9l3-3 5 5-3 3M10 13l2-2M13 16l2-2"/></svg></div>Network &amp;<br>Electrical Cabling</div>
      <div class="service"><div class="service__ring"><svg width="26" height="26" viewBox="0 0 26 26"><path d="M23 3 3 12l8 3 3 8z"/><path d="M11 15 23 3"/></svg></div>Email<br>Archiving</div>
      <div class="service"><div class="service__ring"><svg width="26" height="26" viewBox="0 0 26 26"><path d="M4 8h18v4H4z"/><circle cx="13" cy="17" r="5"/><circle cx="13" cy="17" r="2"/></svg></div>Security cameras<br>&amp; Access Control</div>
    </div>
  </div>

  <div class="panel panel--right">
    <div class="bar" style="left:0;top:18px;width:232px">Cloud Video Telephony</div>
    <ul class="abs ticks" style="left:16px;top:50px;line-height:22.6px">
      <li><svg width="9" height="9"><use href="#tick"/></svg>HD Speakerphone</li>
      <li><svg width="9" height="9"><use href="#tick"/></svg>HD Video</li>
      <li><svg width="9" height="9"><use href="#tick"/></svg>Touch screen available</li>
      <li><svg width="9" height="9"><use href="#tick"/></svg>Supports Wireless Headsets</li>
      <li><svg width="9" height="9"><use href="#tick"/></svg>Built in camera &amp; privacy shutter</li>
      <li><svg width="9" height="9"><use href="#tick"/></svg>Integrates with our other phone services</li>
      <li><svg width="9" height="9"><use href="#tick"/></svg>Ideal for remote workers</li>
      <li style="letter-spacing:-.2px"><svg width="9" height="9"><use href="#tick"/></svg>Video Conference Room solutions available</li>
    </ul>
    <svg class="abs" style="left:0;top:330px" width="256" height="208" viewBox="0 0 256 208">
      <path d="M10 208 Q20 60 256 40" stroke="var(--slate)" stroke-width="4" fill="none"/>
    </svg>
    <div class="photo" role="img" aria-label="Team in a bright meeting room listening to a presenter at a whiteboard" style="left:14px;top:384px;width:242px;height:154px;border-top-left-radius:60% 50%;background:linear-gradient(160deg,#f4f6f8,#c9d3dc 50%,#7f8d9a)"></div>
    <div class="photo" role="img" aria-label="Video desk phone showing a caller on screen" style="left:36px;top:324px;width:96px;height:96px;border-radius:50%;border:5px solid #fff;box-shadow:0 0 0 3px #c8ced4;background:radial-gradient(circle,#3a424b,#12161b 60%,#eef0f2 61%)"></div>
  </div>
</section>

</body>
</html>
```